Tandry Electric service department flyer

Looking to design a electrical service department flyer. The company has been in San Francisco for 60yrs primarily doing work in the downtown area. https://tandryelectric.example/about-tandry/
I attached a rough draft of the flyer. I would like to see something with the san francisco downtown skyline watermarked on the front page, open to the second page that describes all services and contact.

```html
<!DOCTYPE html>
<html lang="en">
<head>
<meta charset="utf-8">
<title>Tandry Electric – Service Department Flyer</title>
<link rel="stylesheet" href="https://fonts.googleapis.com/css2?family=Fraunces:opsz,wght@9..144,600;9..144,700&family=Poppins:wght@400;500;600;700&display=swap">
<style>
  :root{
    --blue:#0051a8;
    --blue-dark:#003f86;
    --white:#ffffff;
    --ink:#111111;
    --stage:#d6d6d6;
  }
  *{box-sizing:border-box;margin:0;padding:0}
  html,body{width:1200px;height:926px;overflow:hidden;background:var(--stage)}
  body{position:relative;font-family:"Poppins",sans-serif;color:var(--ink)}
  .page{position:absolute;top:139px;width:469px;height:648px;background:var(--white);overflow:hidden}
  .page--front{left:100px}
  .page--back{left:637px;width:462px}
  .abs{position:absolute}

  /* FRONT */
  .front-band{left:0;top:0;width:469px;height:293px;background:var(--blue)}
  .hero-photo{left:0;top:0;width:469px;height:250px}
  .logo-box{background:var(--white);display:flex;align-items:center;justify-content:center;text-align:center;gap:8px}
  .logo-box .logo-name{font-family:"Poppins",sans-serif;font-weight:700;color:var(--blue);line-height:1.05;text-transform:uppercase;letter-spacing:1px}
  .logo-box .logo-dot{width:14px;height:14px;background:var(--blue);flex:none}
  .front-logo{left:36px;top:197px;width:185px;height:96px;border-radius:6px 6px 0 0}
  .front-logo .logo-name{font-size:22px}
  .front-title{left:0;top:312px;width:469px;text-align:center;font-family:"Fraunces",serif;font-weight:600;font-size:40px;color:var(--blue);letter-spacing:-0.5px}
  .front-intro{left:40px;top:362px;width:389px;text-align:center;font-size:10.2px;line-height:12.2px}
  .divider-title{left:17px;top:402px;width:435px;height:26px;border-top:1px solid var(--ink);border-bottom:1px solid var(--ink);text-align:center;font-size:17px;font-weight:500;line-height:25px;letter-spacing:.3px}
  .section-tag{top:436px;height:20px;background:var(--blue);color:var(--white);font-size:13px;font-weight:500;line-height:20px;padding-left:19px}
  .tag-services{left:0;width:143px}
  .tag-commercial{left:259px;width:210px;padding-left:10px}
  .check-list{list-style:none;font-size:10.8px;line-height:12px}
  .check-list li{position:relative;padding-left:12px}
  .check-list li::before{content:"✓";position:absolute;left:0;top:2px;width:7px;height:7px;border:1px solid var(--ink);font-size:7px;line-height:6px;text-align:center;font-weight:700}
  .list-services{left:18px;top:464px;width:215px}
  .list-services li{margin-bottom:4.5px}
  .list-commercial{left:263px;top:460px;width:206px}
  .list-commercial li{margin-bottom:6.4px}
  .front-foot-right{left:205px;top:556px;width:264px;height:92px;background:var(--blue)}
  .front-foot{left:0;top:616px;width:469px;height:32px;background:var(--blue)}
  .work-photo{top:562px;width:121px;height:80px;border:3px solid var(--white)}
  .work-photo--a{left:214px;background:linear-gradient(135deg,#b5a89a,#6a6a6e 55%,#3b3e44)}
  .work-photo--b{left:340px;background:linear-gradient(135deg,#8d9196,#4b5158 50%,#25292e)}

  /* BACK */
  .back-band{left:0;top:0;width:462px;height:101px;background:var(--blue)}
  .back-logo{left:22px;top:21px;width:183px;height:80px;border-radius:6px 6px 0 0}
  .back-logo .logo-name{font-size:21px}
  .headline{left:0;width:462px;text-align:center;font-family:"Fraunces",serif;font-weight:700;color:var(--blue);letter-spacing:-1px}
  .why-title{top:140px;font-size:38px}
  .hours-title{top:255px;font-size:38px}
  .reason{height:20px;background:var(--blue);color:var(--white);font-size:8.6px;font-weight:500;line-height:20px;white-space:nowrap}
  .reason--l1{left:0;top:197px;width:224px;padding-left:16px;clip-path:polygon(0 0,100% 0,94% 100%,0 100%)}
  .reason--l2{left:0;top:223px;width:212px;padding-left:16px;clip-path:polygon(0 0,100% 0,94% 100%,0 100%)}
  .reason--r1{left:238px;top:197px;width:224px;padding-left:14px;clip-path:polygon(6% 0,100% 0,100% 100%,0 100%)}
  .reason--r2{left:227px;top:223px;width:235px;padding-left:19px;clip-path:polygon(6% 0,100% 0,100% 100%,0 100%)}
  .hours-cell{height:32px;background:var(--blue);color:var(--white);font-size:16.5px;font-weight:500;text-align:center;line-height:32px}
  .hours-cell--day{left:73px;top:306px;width:124px}
  .hours-cell--time{left:203px;top:306px;width:169px}
  .hours-cell--em{left:73px;top:343px;width:124px;height:26px;line-height:26px}
  .hours-cell--svc{left:203px;top:343px;width:169px;height:26px;line-height:26px}
  .hours-phone{left:73px;top:372px;width:299px;height:26px;border:1px solid var(--blue);color:var(--blue);font-size:16.5px;font-weight:600;text-align:center;line-height:24px;border-radius:2px}
  .estimate-title{top:410px;font-size:29px;font-weight:600;letter-spacing:-0.5px}
  .estimate-strip{left:59px;top:447px;width:343px;height:21px;background:var(--blue);color:var(--white);font-size:12.4px;font-weight:600;text-align:center;line-height:21px}
  .feature-row{display:flex;gap:14px;font-size:11px;list-style:none}
  .feature-row li{position:relative;padding-left:15px}
  .feature-row li::before{content:"✓";position:absolute;left:0;top:3px;width:7px;height:7px;border:1px solid var(--ink);font-size:7px;line-height:6px;text-align:center;font-weight:700}
  .feature-row--1{left:35px;top:480px}
  .feature-row--2{left:57px;top:502px}
  .back-foot{left:0;top:565px;width:462px;height:83px;background:var(--blue)}
  .contact-tag{left:172px;top:552px;width:118px;height:22px;background:var(--white);border:1.5px solid var(--blue);border-bottom:none;font-size:13px;font-weight:500;text-align:center;line-height:22px}
  .contact-item{display:flex;align-items:center;gap:8px;color:var(--white);font-size:10.8px;line-height:12px}
  .contact-item svg{width:14px;height:14px;flex:none}
  .c-phone{left:14px;top:587px}
  .c-mail{left:14px;top:615px}
  .c-web{left:259px;top:586px}
  .c-pin{left:259px;top:614px}
</style>
</head>
<body>

<section class="page page--front">
  <div class="abs front-band"></div>
  <svg class="abs hero-photo" viewBox="0 0 469 250" role="img" aria-label="Photo: electrician in hard hat and safety glasses beside an open electrical panel">
    <defs>
      <linearGradient id="heroGrad" x1="0" y1="0" x2="1" y2="1">
        <stop offset="0" stop-color="#8e9197"/>
        <stop offset=".55" stop-color="#4a4d53"/>
        <stop offset="1" stop-color="#24262b"/>
      </linearGradient>
    </defs>
    <path d="M0 0H469V95C455 150 440 210 425 240Q415 250 395 246L0 110Z" fill="url(#heroGrad)" stroke="#ffffff" stroke-width="3"/>
  </svg>
  <div class="abs logo-box front-logo"><span class="logo-dot"></span><span class="logo-name">Tandry<br>Electric</span></div>

  <h1 class="abs front-title">Tandry Electric</h1>
  <p class="abs front-intro">is a licensed electrical contractor proudly serving San Francisco and surrounding Bay Area communities. Our experienced electricians provide safe, efficient, and code-compliant electrical solutions for residential and</p>
  <div class="abs divider-title">ELECTRICAL / DATACOM</div>

  <div class="abs section-tag tag-services">OUR SERVICES</div>
  <div class="abs section-tag tag-commercial">COMMERCIAL ELECTRICAL</div>

  <ul class="abs check-list list-services">
    <li>Residential Electrical</li>
    <li>Electrical repairs &amp; troubleshooting</li>
    <li>Panel upgrades &amp; breaker<br>replacement</li>
    <li>EV charger installation</li>
    <li>Rewiring &amp; remodels</li>
    <li>Emergency electrical services</li>
    <li>Lighting installation<br>(indoor &amp; outdoor)</li>
  </ul>
  <ul class="abs check-list list-commercial">
    <li>Office &amp; retail electrical systems</li>
    <li>Electrical inspections</li>
    <li>Lighting upgrades &amp; maintenance</li>
    <li>Tenant improvements</li>
    <li>Emergency electrical services</li>
  </ul>

  <div class="abs front-foot-right"></div>
  <div class="abs front-foot"></div>
  <div class="abs work-photo work-photo--a" role="img" aria-label="Photo: electrician in orange hard hat working on a wired panel"></div>
  <div class="abs work-photo work-photo--b" role="img" aria-label="Photo: electrician in orange hard hat servicing a switchgear cabinet"></div>
</section>

<section class="page page--back">
  <div class="abs back-band"></div>
  <div class="abs logo-box back-logo"><span class="logo-dot"></span><span class="logo-name">Tandry<br>Electric</span></div>

  <h2 class="abs headline why-title">WHY CHOOSE US</h2>
  <div class="abs reason reason--l1">CUSTOMER SERVICE IS OUR PRIORITY</div>
  <div class="abs reason reason--r1">PROFESSIONAL, CLEAN AND EFFICIENT WORK</div>
  <div class="abs reason reason--l2">HONEST PRICING &amp; DEPENDABLE RESULTS</div>
  <div class="abs reason reason--r2">SAN FRANCISCO BASED COMPANY SINCE 1966</div>

  <h2 class="abs headline hours-title">HOURS</h2>
  <div class="abs hours-cell hours-cell--day">MON-FRI:</div>
  <div class="abs hours-cell hours-cell--time">8:00 AM - 5:00 PM</div>
  <div class="abs hours-cell hours-cell--em">EMERGENCY</div>
  <div class="abs hours-cell hours-cell--svc">SERVICE AVAILABLE</div>
  <div class="abs hours-phone">24/7 (415) 555-0142</div>

  <h2 class="abs headline estimate-title">Free Estimates Available</h2>
  <div class="abs estimate-strip">Residential · Commercial · 24/7 Emergency Service</div>
  <ul class="abs feature-row feature-row--1">
    <li>Electrical Repairs</li>
    <li>Panel Upgrades</li>
    <li>EV Charger Installation</li>
  </ul>
  <ul class="abs feature-row feature-row--2">
    <li>Lighting Installation</li>
    <li>Building maintenance / 24/7 Service</li>
  </ul>

  <div class="abs back-foot"></div>
  <div class="abs contact-tag">CONTACT US</div>

  <div class="abs contact-item c-phone">
    <svg viewBox="0 0 14 14"><circle cx="7" cy="7" r="7" fill="#fff"/><rect x="4.6" y="3" width="4.8" height="8" rx="1" fill="#0051a8"/><circle cx="7" cy="9.6" r=".6" fill="#fff"/></svg>
    <span>(415) 555-0142</span>
  </div>
  <div class="abs contact-item c-mail">
    <svg viewBox="0 0 14 14"><circle cx="7" cy="7" r="7" fill="#fff"/><rect x="3.5" y="4.5" width="7" height="5" fill="none" stroke="#0051a8" stroke-width="1"/><path d="M3.5 4.5L7 7.3L10.5 4.5" fill="none" stroke="#0051a8" stroke-width="1"/></svg>
    <span>service@tandryelectric.example</span>
  </div>
  <div class="abs contact-item c-web">
    <svg viewBox="0 0 14 14"><circle cx="7" cy="7" r="7" fill="#fff"/><circle cx="7" cy="7" r="4" fill="none" stroke="#0051a8"/><ellipse cx="7" cy="7" rx="1.7" ry="4" fill="none" stroke="#0051a8"/><path d="M3 7H11" stroke="#0051a8"/></svg>
    <span>www.tandryelectric.example</span>
  </div>
  <div class="abs contact-item c-pin">
    <svg viewBox="0 0 14 14"><circle cx="7" cy="7" r="7" fill="#fff"/><path d="M7 11.5C5 9 4.3 7.6 4.3 6.2A2.7 2.7 0 0 1 9.7 6.2C9.7 7.6 9 9 7 11.5Z" fill="#0051a8"/><circle cx="7" cy="6.2" r="1" fill="#fff"/></svg>
    <span>210 Harlan Street, San Francisco,<br>CA 94103</span>
  </div>
</section>

</body>
</html>
```